Bold Website Redesign for a Disruptive Training Brand

Brightmoor Labs is a bold, no-fluff sales & leadership training company powered by AI-driven practice and behavioral science. We’ve already built our website structure and copy in Craftly.io — now we need a designer to fully transform the visual design across all pages (Home, Approach, Programs, About, Contact).
We’re looking for a modern, memorable, high-performance aesthetic that blends human energy, science, and tech without feeling corporate or safe. Clean, bold typography, fluid layout, strong emotional hero moments, subtle motion, and imagery that mixes real people with abstract scientific/tech visuals.Because our clients are primarily North American, please ensure any human photography or AI-generated imagery reflects a North American business context and demographics (modern, diverse, and realistic).

Your job is visual redesign only — no coding required.
The final design must be practical to rebuild inside Craftly.io.

A full, detailed creative brief (plus logo files) is included in the uploaded files.
If you can bring a mix of edge, intelligence, and strong visual storytelling, we’d love to see your work.

Website is already built in Craftly.io at - https://brightmoor-website-tempdesign.craftly.app — structure is set, visuals need redesign.

```html
<!DOCTYPE html>
<html lang="en">
<head>
<meta charset="utf-8">
<title>Brightmoor Labs — Training That Practices Back</title>
<link href="https://fonts.googleapis.com/css2?family=Poppins:wght@400;500;600;700;800&display=swap" rel="stylesheet">
<style>
:root{
  --navy:#0b1c3d;
  --navy-deep:#081631;
  --blue:#1f6fe0;
  --blue-bright:#2f8cff;
  --cyan:#5fc8f2;
  --sky:#dcebfa;
  --ink:#0f1a2e;
  --muted:#5d6a80;
  --line:#e3e9f2;
  --white:#ffffff;
}
*{box-sizing:border-box;margin:0;padding:0}
html,body{width:1200px;height:3188px;overflow:hidden}
body{font-family:"Poppins",sans-serif;color:var(--ink);background:var(--white);position:relative}
section,header,footer{position:absolute;left:0;width:1200px}
.brand{display:flex;align-items:center;gap:8px;font-weight:700;font-size:15px;color:var(--blue);letter-spacing:.02em}
.brand-dot{width:14px;height:14px;border-radius:50%;background:var(--blue)}
.btn{display:inline-flex;align-items:center;gap:6px;font-size:11px;font-weight:600;border-radius:6px;padding:9px 16px;text-decoration:none}
.btn-primary{background:var(--blue);color:var(--white)}
.btn-light{background:var(--white);color:var(--ink)}
.btn-ghost{border:1px solid rgba(255,255,255,.7);color:var(--white)}

/* nav */
.site-nav{top:0;height:56px;background:var(--white);display:flex;align-items:center;justify-content:space-between;padding:0 60px;border-bottom:1px solid var(--line)}
.nav-links{display:flex;gap:34px;font-size:11px;color:var(--ink)}
.nav-cta{display:flex;align-items:center;gap:18px;font-size:11px}
.nav-phone{display:flex;align-items:center;gap:6px}

/* hero */
.hero{top:56px;height:470px;overflow:hidden;text-align:center;color:var(--white)}
.hero-art{position:absolute;inset:0;background:linear-gradient(180deg,#8fb2d6 0%,#6f9ccc 45%,#b9d3ec 80%,#eef5fc 100%)}
.hero-inner{position:relative;padding-top:80px}
.hero h1{font-size:50px;font-weight:800;line-height:1.05;letter-spacing:.01em}
.hero-sub{font-size:13px;font-weight:600;margin-top:16px}
.hero-copy{font-size:11px;line-height:1.6;max-width:520px;margin:26px auto 0;opacity:.92}
.hero-actions{display:flex;gap:12px;justify-content:center;margin-top:26px}

/* problem */
.problem{top:526px;height:830px}
.problem h2{position:absolute;left:160px;top:80px;width:400px;font-size:28px;font-weight:700;line-height:1.2}
.problem p{position:absolute;left:640px;top:76px;width:400px;font-size:11px;line-height:1.65;color:var(--muted)}
.problem .note{position:absolute;left:640px;top:170px;font-size:10px;color:var(--blue);font-weight:600}
.dash-frame{position:absolute;left:160px;top:240px;width:880px;height:560px;border-radius:18px;background:linear-gradient(135deg,#7fd6f5 0%,#3b8ef0 55%,#1f5fd6 100%)}
.dash{position:absolute;left:60px;top:46px;width:760px;height:470px;background:var(--white);border-radius:12px;box-shadow:0 20px 50px rgba(10,30,80,.25);display:flex;overflow:hidden}
.dash-side{width:120px;border-right:1px solid var(--line);padding:18px 14px;font-size:10px;color:var(--muted)}
.dash-side .brand{font-size:11px;margin-bottom:22px}
.dash-side ul{list-style:none}
.dash-side li{padding:7px 8px;border-radius:6px;margin-bottom:4px}
.dash-side li.active{background:var(--blue);color:var(--white)}
.dash-main{flex:1;padding:16px 20px;position:relative}
.dash-top{display:flex;justify-content:space-between;align-items:center;font-size:10px;color:var(--muted)}
.search{width:220px;height:24px;border:1px solid var(--line);border-radius:6px}
.dash-title{font-size:15px;font-weight:600;margin:14px 0 10px}
.stats{display:flex;gap:10px}
.stat{flex:1;border:1px solid var(--line);border-radius:8px;padding:10px;font-size:9px;color:var(--muted)}
.stat b{display:block;font-size:16px;color:var(--ink);margin-top:4px}
.chart-card{position:absolute;left:20px;top:166px;width:360px;height:150px;border:1px solid var(--line);border-radius:8px}
.aud-card{position:absolute;right:20px;top:166px;width:230px;height:196px;border:1px solid var(--line);border-radius:8px;padding:12px;font-size:9px;color:var(--muted);box-shadow:0 10px 24px rgba(20,40,90,.12);background:var(--white)}
.aud-card b{font-size:18px;color:var(--ink)}
.aud-row{display:flex;justify-content:space-between;margin-top:10px}
.table-card{position:absolute;left:20px;top:330px;width:360px;height:124px;border:1px solid var(--line);border-radius:8px;padding:8px 10px;font-size:9px;color:var(--muted)}
.table-card div{display:flex;justify-content:space-between;border-bottom:1px solid var(--line);padding:6px 0}
.table-card div:last-child{border-bottom:0}

/* practice */
.practice{top:1356px;height:530px;background:var(--navy);overflow:hidden;color:var(--white)}
.practice-glow{position:absolute;left:-120px;top:140px;width:700px;height:500px;background:radial-gradient(ellipse at center,rgba(47,140,255,.35),rgba(11,28,61,0) 70%)}
.practice h2{position:absolute;left:160px;top:110px;font-size:28px;font-weight:700}
.practice-copy{position:absolute;left:160px;top:160px;width:360px;font-size:11px;line-height:1.6;opacity:.85}
.practice .btn{position:absolute;left:160px;top:210px}
.pillar{position:absolute;left:680px;width:360px;height:130px;border-radius:10px;background:linear-gradient(135deg,#2f8cff,#54b4f2);display:flex;gap:16px;padding:16px}
.pillar-icon{width:90px;height:98px;border-radius:8px;background:var(--navy-deep);display:flex;align-items:center;justify-content:center;flex-shrink:0}
.pillar h3{font-size:15px;font-weight:700;margin-bottom:6px}
.pillar p{font-size:10px;line-height:1.55;opacity:.95}

/* team */
.team{top:1886px;height:500px;background:var(--white)}
.team-photo{position:absolute;left:160px;top:80px;width:880px;height:360px;border-radius:10px;background:linear-gradient(135deg,#c8d2dc 0%,#8a98a8 45%,#c7a98a 75%,#e8e0d4 100%)}
.team-card{position:absolute;left:600px;top:260px;width:440px;height:180px;background:var(--navy);color:var(--white);padding:24px 30px;border-radius:10px 0 10px 0}
.team-card h2{font-size:20px;font-weight:700;line-height:1.25}
.team-card p{font-size:10px;line-height:1.6;opacity:.85;margin-top:8px}
.team-card .btn{margin-top:10px;padding:6px 12px}

/* cta */
.cta{top:2386px;height:450px;background:linear-gradient(180deg,var(--navy-deep),#0e2550);overflow:hidden;text-align:center;color:var(--white)}
.cta-glow{position:absolute;left:300px;top:120px;width:600px;height:360px;background:radial-gradient(ellipse at center,rgba(47,140,255,.3),rgba(8,22,49,0) 70%)}
.cta h2{position:relative;font-size:26px;font-weight:700;line-height:1.2;margin-top:56px}
.cta .btn{position:relative;margin-top:18px}

/* footer */
.site-footer{top:2836px;height:352px;background:var(--white);padding:0 60px}
.foot-top{display:flex;justify-content:space-between;align-items:center;padding-top:40px;border-bottom:1px solid var(--line);padding-bottom:30px}
.foot-links{display:flex;gap:32px;font-size:11px}
.foot-info{display:flex;justify-content:space-between;padding-top:24px;font-size:10px;color:var(--muted);line-height:1.6}
.foot-info h4{color:var(--ink);font-size:11px;font-weight:600;margin-bottom:4px}
.socials{display:flex;gap:12px;align-items:center}
.socials span{width:18px;height:18px;border-radius:50%;background:var(--ink)}
.foot-base{display:flex;justify-content:space-between;margin-top:40px;padding-top:14px;border-top:1px solid var(--line);font-size:9px;color:var(--muted)}
</style>
</head>
<body>

<header class="site-nav">
  <div class="brand"><span class="brand-dot"></span>BRIGHTMOOR LABS</div>
  <nav class="nav-links"><span>Home</span><span>About</span><span>Approach</span><span>Programs</span><span>Contact</span></nav>
  <div class="nav-cta">
    <span class="nav-phone"><svg width="12" height="12" viewBox="0 0 24 24"><path d="M6.6 10.8a15 15 0 0 0 6.6 6.6l2.2-2.2a1 1 0 0 1 1-.25 11.4 11.4 0 0 0 3.6.57 1 1 0 0 1 1 1V20a1 1 0 0 1-1 1A17 17 0 0 1 3 4a1 1 0 0 1 1-1h3.5a1 1 0 0 1 1 1c0 1.25.2 2.45.57 3.6a1 1 0 0 1-.25 1z" fill="#0f1a2e"/></svg>+1 (555) 218-4470</span>
    <a class="btn btn-primary">Let's Talk</a>
  </div>
</header>

<section class="hero">
  <div class="hero-art" role="img" aria-label="Abstract flowing blue wave artwork behind the headline"></div>
  <div class="hero-inner">
    <h1>TRAINING THAT<br>PRACTICES BACK.</h1>
    <p class="hero-sub">AI-driven sustainment that builds mastery — so your team won't forget it.</p>
    <p class="hero-copy">You'll never measure growth by one workshop again. Our practice engine keeps every skill alive long after day one, turning short training moments into lasting behavior your leaders can see.</p>
    <div class="hero-actions"><a class="btn btn-light">Book a Demo →</a><a class="btn btn-ghost">See How It Works</a></div>
  </div>
</section>

<section class="problem">
  <h2>The real problem isn't your people — it's the forgetting curve.</h2>
  <p>Within a week, most training disappears. Leaders are left guessing which ideas stuck and which faded. Brightmoor Labs uses science-backed practice to keep progress, confidence, and results growing week after week.</p>
  <span class="note">See how sustained practice works →</span>
  <div class="dash-frame">
    <div class="dash">
      <div class="dash-side">
        <div class="brand"><span class="brand-dot"></span>Brightmoor</div>
        <ul><li class="active">Dashboard</li><li>Practice</li><li>Reports</li><li>Settings</li><li>Help</li></ul>
      </div>
      <div class="dash-main">
        <div class="dash-top"><div class="search"></div><span>Dana Reyes</span></div>
        <div class="dash-title">Overview</div>
        <div class="stats">
          <div class="stat">Total Engagement<b>4,650</b></div>
          <div class="stat">Active Learners<b>9,500</b></div>
          <div class="stat">Practice Sessions<b>12,480</b></div>
          <div class="stat">Retention<b>76.5%</b></div>
        </div>
        <div class="chart-card">
          <svg width="360" height="150" viewBox="0 0 360 150" aria-label="Weekly practice line chart">
            <path d="M10 122 L50 104 L90 112 L130 76 L170 88 L210 58 L250 68 L290 40 L340 48 V142 H10Z" fill="rgba(47,140,255,.15)"/>
            <path d="M10 122 L50 104 L90 112 L130 76 L170 88 L210 58 L250 68 L290 40 L340 48" fill="none" stroke="#2f8cff" stroke-width="2"/>
            <text x="12" y="20" font-family="Poppins,sans-serif" font-size="10" fill="#5d6a80">Weekly practice</text>
          </svg>
        </div>
        <div class="aud-card">
          Overall Audience<br><b>20,463</b>
          <svg width="206" height="50" viewBox="0 0 206 50"><rect x="0" y="30" width="20" height="20" fill="#2f8cff"/><rect x="30" y="18" width="20" height="32" fill="#5fc8f2"/><rect x="60" y="24" width="20" height="26" fill="#2f8cff"/><rect x="90" y="8" width="20" height="42" fill="#5fc8f2"/><rect x="120" y="20" width="20" height="30" fill="#2f8cff"/><rect x="150" y="12" width="20" height="38" fill="#5fc8f2"/><rect x="180" y="26" width="20" height="24" fill="#2f8cff"/></svg>
          <div class="aud-row"><span>Email</span><span>10,540</span></div>
          <div class="aud-row"><span>Mobile</span><span>6,210</span></div>
          <div class="aud-row"><span>Web</span><span>3,713</span></div>
        </div>
        <div class="table-card">
          <div><span>Team</span><span>Sessions</span><span>Score</span></div>
          <div><span>Sales East</span><span>1,204</span><span>88%</span></div>
          <div><span>Leadership</span><span>860</span><span>91%</span></div>
          <div><span>Support</span><span>642</span><span>79%</span></div>
        </div>
      </div>
    </div>
  </div>
</section>

<section class="practice">
  <div class="practice-glow"></div>
  <h2>Practice made permanent.</h2>
  <p class="practice-copy">You'll replace "hope they remember" with a system that makes sure they do.</p>
  <a class="btn btn-ghost">See How We Do It →</a>
  <div class="pillar" style="top:84px">
    <div class="pillar-icon"><svg width="40" height="40" viewBox="0 0 40 40"><circle cx="20" cy="20" r="14" fill="none" stroke="#5fc8f2" stroke-width="3"/><path d="M20 12v8l6 4" stroke="#5fc8f2" stroke-width="3" fill="none"/></svg></div>
    <div><h3>Learn</h3><p>Real conversations, real feedback: we start with new behaviors practiced in the moments that matter most.</p></div>
  </div>
  <div class="pillar" style="top:230px">
    <div class="pillar-icon"><svg width="40" height="40" viewBox="0 0 40 40"><path d="M4 32 L14 20 L22 26 L36 8" fill="none" stroke="#5fc8f2" stroke-width="3"/></svg></div>
    <div><h3>Certify</h3><p>Programmable AI drives practice and feedback, tracking skill growth against real benchmarks.</p></div>
  </div>
  <div class="pillar" style="top:376px">
    <div class="pillar-icon"><svg width="40" height="40" viewBox="0 0 40 40"><path d="M8 20 l8 8 l16 -16" fill="none" stroke="#5fc8f2" stroke-width="3"/></svg></div>
    <div><h3>Sustain</h3><p>Light-touch challenges and reinforcement that keep skills sharp long after training ends.</p></div>
  </div>
</section>

<section class="team">
  <div class="team-photo" role="img" aria-label="Photo of several hands joining jigsaw puzzle pieces together over a table"></div>
  <div class="team-card">
    <h2>Built by people who've led the change themselves.</h2>
    <p>Behind Brightmoor Labs are leaders who have lived the challenge of making learning last, and designed a system that finally delivers.</p>
    <a class="btn btn-ghost">Meet our team →</a>
  </div>
</section>

<section class="cta">
  <div class="cta-glow"></div>
  <h2>READY TO SEE WHAT LASTING<br>CAPABILITY LOOKS LIKE?</h2>
  <a class="btn btn-primary">Book a Demo →</a>
</section>

<footer class="site-footer">
  <div class="foot-top">
    <div class="brand"><span class="brand-dot"></span>BRIGHTMOOR LABS</div>
    <nav class="foot-links"><span>Home</span><span>About</span><span>Approach</span><span>Programs</span><span>Contact</span></nav>
    <a class="btn btn-primary">Let's Talk</a>
  </div>
  <div class="foot-info">
    <div><h4>Address</h4>1480 Harbor Ridge Rd, Suite 210<br>Tempe, AZ 85281</div>
    <div><h4>Phone</h4>+1 (555) 218-4470</div>
    <div><h4>Email</h4>hello@brightmoorlabs.com</div>
    <div class="socials" aria-label="Social links"><span></span><span></span></div>
  </div>
  <div class="foot-base"><span>© 2025 Brightmoor Labs. All rights reserved.</span><span>Terms · Privacy</span></div>
</footer>

</body>
</html>
```